TKR Advisory Business Cards

Hi there,

I'd like to make a simple new business card design with the logo we already have created for our business.

I need a double sided business card with our logo on the front side and the company and person's details on the back side.

I'd like it to be on a white background and no background so I can potentially use it with either white paper or put it on different coloured paper in accordance with our business colours.

Please use the logo images I have attached and also the fonts.

So Front side:
- Logo in centre of business card (use medium logo so there is a pretty decent border around it, so don't want to fill the whole card but to make it prominent).

Back Side.
- We need 3 different business cards with the different people's name on each.

ie.

Dorian Halvreck
Business Development Manager

m +61 437 206 518
e dorian@tkradvisory.com.au
w tkradvisory.com.au

- Also I'd like to put only the cog/power button logo in the top right hand corner of the card.
(You might need to chop the current logo in half as I don't have a seperate log just for this)
- Also I'd like some lines running on the top left hand corner diagonally, anything that will add to the design or some swirling lines that add some cool effect to the card.

Also I'd like to maybe put our ABN in the bottom right hand corner of the card in a smaller font.

I'd like to also talk to the designer if possible so I can get my idea across a bit better.

Thanks!

Regards,
Dorian

```html
<!DOCTYPE html>
<html lang="en">
<head>
<meta charset="utf-8">
<title>TKR Advisory – Business Card</title>
<link rel="stylesheet" href="https://fonts.googleapis.com/css2?family=Exo+2:wght@600&family=Michroma&family=Syncopate:wght@400;700&display=swap">
<style>
  :root {
    --card-white: #ffffff;
    --ink: #1e1e1e;
    --corner-black: #000000;
    --corner-warm: #3a1d08;
    --badge-grey: #4a4a4a;
  }
  html, body {
    margin: 0;
    padding: 0;
    width: 1200px;
    height: 741px;
    overflow: hidden;
    background: var(--card-white);
  }
  .card {
    position: relative;
    width: 1200px;
    height: 741px;
    background: var(--card-white);
    color: var(--ink);
    overflow: hidden;
  }
  .corner-accent {
    position: absolute;
    left: 0;
    top: 0;
  }
  .brand {
    position: absolute;
    top: 48px;
    right: 24px;
    display: flex;
    align-items: center;
    gap: 12px;
  }
  .brand-name {
    font-family: "Exo 2", sans-serif;
    font-weight: 600;
    font-size: 24px;
    color: var(--ink);
    white-space: nowrap;
  }
  .brand-dot {
    width: 156px;
    height: 156px;
    border-radius: 50%;
    background: var(--badge-grey);
  }
  .person {
    position: absolute;
    left: 0;
    right: 0;
    top: 220px;
    text-align: center;
  }
  .person-name {
    margin: 0;
    font-family: "Exo 2", sans-serif;
    font-weight: 600;
    font-size: 60px;
    line-height: 66px;
    color: var(--ink);
  }
  .person-role {
    margin: 8px 0 0;
    font-family: "Syncopate", "Michroma", sans-serif;
    font-weight: 400;
    font-size: 28px;
    line-height: 36px;
    letter-spacing: 2px;
    color: var(--ink);
    white-space: nowrap;
  }
  .contact {
    position: absolute;
    left: 71px;
    top: 572px;
    margin: 0;
    padding: 0;
    list-style: none;
    font-family: "Syncopate", "Michroma", sans-serif;
    font-size: 19px;
    letter-spacing: 1.5px;
    line-height: 35px;
    color: var(--ink);
    white-space: nowrap;
  }
  .contact-label {
    margin-right: 8px;
  }
  .abn {
    position: absolute;
    left: 741px;
    top: 615px;
    margin: 0;
    font-family: "Syncopate", "Michroma", sans-serif;
    font-weight: 700;
    font-size: 21px;
    line-height: 30px;
    letter-spacing: 2px;
    color: var(--ink);
    white-space: nowrap;
  }
</style>
</head>
<body>
  <main class="card">
    <svg class="corner-accent" width="250" height="380" viewBox="0 0 250 380" role="img" aria-label="Black corner with swirling orange line decoration">
      <defs>
        <linearGradient id="corner-tone" x1="0" y1="0" x2="1" y2="1">
          <stop offset="0" stop-color="var(--corner-warm)"/>
          <stop offset="0.6" stop-color="var(--corner-black)"/>
        </linearGradient>
      </defs>
      <polygon points="0,0 245,0 0,376" fill="url(#corner-tone)"/>
    </svg>

    <div class="brand">
      <span class="brand-name">TKR Advisory</span>
      <span class="brand-dot"></span>
    </div>

    <header class="person">
      <h1 class="person-name">Dorian Halvreck</h1>
      <p class="person-role">Business Development Manager</p>
    </header>

    <ul class="contact">
      <li><span class="contact-label">m</span>+61 437 206 518</li>
      <li><span class="contact-label">e</span>dorian@tkradvisory.com.au</li>
      <li><span class="contact-label">w</span>tkradvisory.com.au</li>
    </ul>

    <p class="abn">ABN: 4827 1953 306</p>
  </main>
</body>
</html>
```